Spirits Bottle Label-Brand Name Reed & Barrow

Design a spirits bottle label per specifications outlined. Label size Front 3.875x 4.5,Back 2x4, topper 1x5.7. Must have established 2020, 40% Alcohol by volume. 40 proof. Sherry Cask Settled. Bottle # 1 of 1320. Caribbean Rum. Trademark logo must be on the label. Back of label has to have all the information outlined in photo. Topper & Front of the label the designer can you his creativity. Color scheme is negotiable and designers can be creative.

Target Market(s)

Adults aged 21 with an appealing appearance that caters to a young professionals and seasoned adults

Font styles to use
Sans Serif

Colors
886aae
33b8a4
33a6d7

Requirements
Must have
• -Reed & Barrow Trademark Logo which is attached.
-Caribbean Rum
-40% Alcohol By Volume
-80 Proof
-Sherry Cask Settled
-Established 2020

```html
<!DOCTYPE html>
<html lang="en">
<head>
<meta charset="utf-8">
<title>Reed &amp; Barrow – Caribbean Rum Front Label</title>
<link href="https://fonts.googleapis.com/css2?family=Oswald:wght@600&family=Libre+Baskerville:wght@400;700&family=Yellowtail&family=Archivo+Black&family=Roboto:wght@400&family=Caveat&display=swap" rel="stylesheet">
<style>
  :root {
    --page: #ffffff;
    --paper: #f2f0e3;
    --teal: #6db6a5;
    --teal-script: #7cc2b0;
    --ink: #2f2f2f;
    --white: #ffffff;
  }
  html, body {
    margin: 0;
    width: 1200px;
    height: 1200px;
    overflow: hidden;
    background: var(--page);
  }
  .front-label {
    position: absolute;
    left: 140px;
    top: 83px;
    width: 920px;
    height: 1034px;
  }
  .label-paper { fill: var(--paper); }
  .label-frame { fill: none; stroke: var(--teal); stroke-width: 10; }
  .footer-band { fill: var(--teal); }
  .scene-art { opacity: 0.55; }
  .mark-circle { fill: none; stroke: var(--ink); stroke-width: 6; }
  .mark-name { font-family: "Oswald", sans-serif; font-weight: 600; font-size: 34px; fill: var(--ink); }
  .tag-box { fill: var(--ink); }
  .tag-text { font-family: "Libre Baskerville", serif; font-size: 24px; fill: var(--paper); }
  .brand-name { font-family: "Oswald", sans-serif; font-weight: 600; font-size: 124px; fill: var(--ink); }
  .authentic { font-family: "Libre Baskerville", serif; font-size: 34px; letter-spacing: 5px; fill: var(--ink); }
  .dot { fill: var(--ink); }
  .spirit-type { font-family: "Yellowtail", cursive; font-size: 108px; fill: var(--teal-script); }
  .batch-line { font-family: "Libre Baskerville", serif; font-size: 38px; letter-spacing: 6px; fill: var(--ink); }
  .rule { stroke: var(--teal); stroke-width: 5; stroke-linecap: round; }
  .proof-number { font-family: "Libre Baskerville", serif; font-weight: 700; font-size: 58px; fill: var(--ink); }
  .proof-word { font-family: "Libre Baskerville", serif; font-size: 24px; letter-spacing: 3px; fill: var(--ink); }
  .cask-badge { fill: var(--paper); }
  .cask-text { font-family: "Archivo Black", sans-serif; font-size: 31px; letter-spacing: 1px; fill: var(--ink); }
  .band-dot { fill: var(--paper); }
  .band-info { font-family: "Roboto", sans-serif; font-size: 21px; fill: var(--white); }
  .number-box { fill: var(--white); }
  .bottle-number { font-family: "Caveat", cursive; font-size: 28px; fill: var(--ink); }
</style>
</head>
<body>
<svg class="front-label" viewBox="0 0 920 1034" xmlns="http://www.w3.org/2000/svg">
  <defs>
    <linearGradient id="sceneTone" x1="0" y1="0" x2="0" y2="1">
      <stop offset="0" stop-color="#dcdfd3"/>
      <stop offset="1" stop-color="#e7e8dc"/>
    </linearGradient>
    <path id="authenticArc" d="M 270 540 Q 463 470 656 540"/>
    <path id="caskArc" d="M 180 866 Q 463 1014 746 866"/>
  </defs>

  <rect class="label-paper" x="0" y="0" width="920" height="1034"/>
  <rect class="scene-art" x="8" y="8" width="904" height="862" fill="url(#sceneTone)"
        role="img" aria-label="Faint pencil sketch of a tropical shore with palm trees and a tall sailing ship"/>
  <rect class="footer-band" x="0" y="878" width="920" height="142"/>
  <rect class="label-frame" x="5" y="5" width="910" height="1024"/>

  <g class="brand-mark">
    <circle class="mark-circle" cx="463" cy="134" r="120"/>
    <text class="mark-name" x="463" y="146" text-anchor="middle">REED &amp; BARROW</text>
  </g>

  <rect class="tag-box" x="62" y="365" width="80" height="50"/>
  <text class="tag-text" x="102" y="399" text-anchor="middle">EST.</text>
  <text class="brand-name" x="463" y="450" text-anchor="middle" textLength="620" lengthAdjust="spacingAndGlyphs">REED &amp; BARROW</text>
  <rect class="tag-box" x="790" y="365" width="83" height="50"/>
  <text class="tag-text" x="831" y="399" text-anchor="middle">2020</text>

  <text class="authentic"><textPath href="#authenticArc" startOffset="50%" text-anchor="middle">AUTHENTIC</textPath></text>
  <g class="dots">
    <circle class="dot" cx="393" cy="552" r="4"/>
    <circle class="dot" cx="418" cy="552" r="5"/>
    <circle class="dot" cx="463" cy="552" r="9"/>
    <circle class="dot" cx="508" cy="552" r="5"/>
    <circle class="dot" cx="533" cy="552" r="4"/>
  </g>

  <text class="spirit-type" x="463" y="680" text-anchor="middle">Caribbean Rum</text>
  <text class="batch-line" x="463" y="748" text-anchor="middle" textLength="640" lengthAdjust="spacing">SMALL BATCH CRAFTED</text>

  <line class="rule" x1="300" y1="800" x2="390" y2="800"/>
  <line class="rule" x1="536" y1="800" x2="626" y2="800"/>
  <text class="proof-number" x="463" y="820" text-anchor="middle">80</text>
  <text class="proof-word" x="463" y="852" text-anchor="middle">PROOF</text>

  <path class="cask-badge" d="M 190 878 L 736 878 Q 700 955 463 982 Q 226 955 190 878 Z"/>
  <text class="cask-text"><textPath href="#caskArc" startOffset="50%" text-anchor="middle">SHERRY CASK SETTLED</textPath></text>
  <g class="band-dots">
    <circle class="band-dot" cx="403" cy="998" r="3"/>
    <circle class="band-dot" cx="428" cy="999" r="5"/>
    <circle class="band-dot" cx="463" cy="1001" r="8"/>
    <circle class="band-dot" cx="498" cy="999" r="5"/>
    <circle class="band-dot" cx="523" cy="998" r="3"/>
  </g>

  <text class="band-info" x="54" y="918">750 ML.</text>
  <text class="band-info" x="54" y="968">ALC. BY VOL. 40%</text>
  <text class="band-info" x="880" y="910" text-anchor="end">BOTTLE NO.</text>
  <rect class="number-box" x="718" y="935" width="162" height="52" rx="8"/>
  <text class="bottle-number" x="799" y="970" text-anchor="middle" textLength="130" lengthAdjust="spacingAndGlyphs">0001 / 1320</text>
</svg>
</body>
</html>
```